Quimby's Yard & Garden Center Business Card Update

I need an updated Business card design for my Lawn and Garden Center. We do Landscaping installs, Lawn Mowing, Snow Removal and also have a Garden Center Retail Division. I uploaded a few of our previous business cards to give an idea of what we are starting with. The main goal of this update is to simplify and modernize the business card, not all of the services that are on the previous cards has to be on the new one but I would still like to highlight our main services. There is also a sample of our logo that Can be used in the design.

Industry/Entity Type

Landscaping

Contact Information for Business Card

Morris Quimby
Morris@Quimbysyardandgarden.example
Business (555) 201-7784
Cell (555) 318-6092

Colors

Designer to choose colors to be used in the design.

Requirements
Must have
• Services Provided :
• Landscaping
• Lawn Maintenance
• Snow Removal
• Garden Center

```html
<!DOCTYPE html>
<html lang="en">
<head>
<meta charset="utf-8">
<title>Quimby's Yard & Garden Center – Business Cards</title>
<link href="https://fonts.googleapis.com/css2?family=Libre+Baskerville:wght@400;700&family=Montserrat:wght@600;700&family=Roboto+Condensed:wght@700&family=Open+Sans:wght@400;700&display=swap" rel="stylesheet">
<style>
  :root{
    --bg:#e6e4e2;
    --green-deep:#0b3d0b;
    --green-dark:#0f4f0f;
    --green-mid:#1b7a1b;
    --green-glow:#1f8a1f;
    --green-leaf:#2e6b2a;
    --green-light:#9fe08a;
    --green-pale:#d6f7d6;
    --white:#ffffff;
    --ink:#0d3d0d;
    --serif:'Libre Baskerville', Georgia, serif;
    --sans:'Montserrat', Arial, sans-serif;
    --cond:'Roboto Condensed', 'Arial Narrow', sans-serif;
    --body:'Open Sans', Arial, sans-serif;
  }
  *{box-sizing:border-box;margin:0;padding:0}
  html,body{width:1200px;height:900px;overflow:hidden;background:var(--bg)}
  .sheet{position:relative;width:1200px;height:900px}
  .card{position:absolute;left:285px;width:630px;height:360px;overflow:hidden;box-shadow:0 6px 18px rgba(0,0,0,.18)}
  .card--front{top:60px;background:radial-gradient(ellipse at 42% 52%, var(--green-glow) 0%, var(--green-dark) 45%, var(--green-deep) 100%)}
  .card--back{top:480px;background:var(--white)}

  /* front */
  .hex{position:absolute}
  .divider{position:absolute;left:305px;top:62px;width:1px;height:180px;background:rgba(159,224,138,.45)}
  .contact{position:absolute;left:48px;top:118px;color:var(--white);font-family:var(--sans);font-weight:700}
  .contact .names{font-size:16px;margin-bottom:6px}
  .contact .row{display:flex;align-items:center;gap:7px;font-size:15px;margin-bottom:4px}
  .contact .row.email{font-size:12.5px}
  .icon{width:14px;height:14px;flex:none}
  .brand{position:absolute;left:340px;top:70px;width:260px;text-align:center;color:var(--white)}
  .brand-name{display:flex;align-items:center;justify-content:center;gap:10px;font-family:var(--serif);font-weight:700;font-size:44px;color:var(--green-light)}
  .brand-dot{width:16px;height:16px;border-radius:50%;background:var(--green-light)}
  .brand-full{font-family:var(--serif);font-size:16px;margin-top:26px}
  .brand-llc{font-family:var(--serif);font-size:13px;text-align:right;margin-top:2px}
  .floral{position:absolute;left:48px;top:285px;color:var(--white);font-family:var(--body);font-size:13px;line-height:1.35}
  .floral strong{font-weight:700;font-size:14px}

  /* back */
  .clover{position:absolute;inset:0;clip-path:polygon(0 0,56% 0,40% 100%,0 100%);background:radial-gradient(circle at 30% 40%, var(--green-leaf), var(--green-deep) 85%)}
  .back-brand{position:absolute;left:30px;top:36px;width:230px;text-align:center}
  .back-brand .brand-name{font-size:34px}
  .back-title{position:absolute;left:24px;top:130px;color:var(--white);font-family:var(--serif);font-weight:700;font-size:30px;line-height:1.12;text-align:center;width:260px}
  .back-title .llc{display:block;text-align:right;font-weight:400;font-size:16px;margin-top:-6px}
  .url{position:absolute;left:26px;top:326px;color:var(--white);font-family:var(--body);font-size:11px}
  .back-contact{position:absolute;left:375px;top:22px;color:var(--ink);font-family:var(--sans);font-weight:700}
  .back-contact .names{font-size:14px;margin-bottom:3px}
  .back-contact .row{display:flex;align-items:center;gap:6px;font-size:13px;margin-bottom:2px}
  .services-tag{position:absolute;left:350px;top:118px;width:250px;height:36px;background:var(--green-dark);color:var(--white);font-family:var(--cond);font-weight:700;font-size:20px;display:flex;align-items:center;padding-left:22px;border-radius:0 18px 18px 0;clip-path:polygon(12px 0,100% 0,100% 100%,0 100%)}
  .services{position:absolute;left:360px;top:166px;list-style:none;color:var(--ink);font-family:var(--sans);font-weight:600;font-size:17px;line-height:1.18}
  .services li::before{content:"•";margin-right:3px}
  .address{position:absolute;left:252px;top:312px;width:378px;height:34px;background:var(--green-dark);color:var(--white);font-family:var(--sans);font-weight:600;font-size:14px;display:flex;align-items:center;gap:6px;padding-left:26px;border-radius:0 17px 17px 0;clip-path:polygon(10px 0,100% 0,100% 100%,0 100%)}
</style>
</head>
<body>
<main class="sheet">

  <section class="card card--front" aria-label="Business card front">
    <svg class="hex" width="630" height="360" viewBox="0 0 630 360" aria-hidden="true">
      <polygon points="400,235 450,225 470,262 440,292 392,285 380,255" fill="#6fcf6f" opacity=".25"/>
      <polygon points="330,300 400,285 420,330 380,360 320,360" fill="#6fcf6f" opacity=".18"/>
    </svg>
    <div class="contact">
      <p class="names">Morris &amp; Jean Quimby</p>
      <p class="row"><svg class="icon" viewBox="0 0 16 16"><circle cx="8" cy="8" r="8" fill="#fff"/><path d="M5 4.5l1.5-.5 1 2-1 .8a5 5 0 0 0 2.7 2.7l.8-1 2 1-.5 1.5c-3.2.3-6.8-3.3-6.5-6.5z" fill="#0f4f0f"/></svg>(555) 201-7784</p>
      <p class="row"><svg class="icon" viewBox="0 0 16 16"><rect x="1" y="5" width="14" height="10" rx="1" fill="#fff"/><rect x="4" y="1" width="7" height="5" fill="#fff" stroke="#0f4f0f"/><rect x="3" y="8" width="6" height="1.5" fill="#0f4f0f"/><rect x="3" y="11" width="6" height="1.5" fill="#0f4f0f"/></svg>(555) 318-6092</p>
      <p class="row email"><svg class="icon" viewBox="0 0 16 16"><circle cx="8" cy="8" r="8" fill="#fff"/><rect x="4" y="5" width="8" height="6" fill="none" stroke="#0f4f0f"/><path d="M4 5l4 3.5L12 5" fill="none" stroke="#0f4f0f"/></svg>jean@quimbysyardandgarden.example</p>
    </div>
    <div class="divider"></div>
    <div class="brand">
      <p class="brand-name"><span class="brand-dot"></span>Quimby's</p>
      <p class="brand-full">Quimby's Yard &amp; Garden Center</p>
      <p class="brand-llc">(LLC)</p>
    </div>
    <div class="floral">
      <p><strong>Full Service Fresh Floral Department</strong></p>
      <p>•Wedding &nbsp;•Funeral &nbsp;•Special Occasions</p>
      <p>•Delivery Service Available</p>
    </div>
  </section>

  <section class="card card--back" aria-label="Business card back">
    <svg class="hex" width="630" height="360" viewBox="0 0 630 360" aria-hidden="true">
      <polygon points="560,0 630,0 630,40 590,60 560,35" fill="#c8f5c8" opacity=".8"/>
      <polygon points="520,200 600,180 630,210 630,300 560,320 500,280" fill="#c8f5c8" opacity=".7"/>
    </svg>
    <div class="clover" role="img" aria-label="Close-up photo of green clover leaves"></div>
    <div class="back-brand">
      <p class="brand-name"><span class="brand-dot"></span>Quimby's</p>
    </div>
    <h1 class="back-title">Quimby's Yard<br>&amp;<br>Garden Center<span class="llc">(LLC)</span></h1>
    <p class="url">https://quimbysyardandgarden.example/</p>

    <div class="back-contact">
      <p class="names">Morris &amp; Jean Quimby</p>
      <p class="row"><svg class="icon" viewBox="0 0 16 16"><circle cx="8" cy="8" r="8" fill="#0f4f0f"/><path d="M5 4.5l1.5-.5 1 2-1 .8a5 5 0 0 0 2.7 2.7l.8-1 2 1-.5 1.5c-3.2.3-6.8-3.3-6.5-6.5z" fill="#fff"/></svg>(555) 201-7784</p>
      <p class="row"><svg class="icon" viewBox="0 0 16 16"><rect x="1" y="5" width="14" height="10" rx="1" fill="#0f4f0f"/><rect x="4" y="1" width="7" height="5" fill="#fff" stroke="#0f4f0f"/><rect x="3" y="8" width="6" height="1.5" fill="#fff"/><rect x="3" y="11" width="6" height="1.5" fill="#fff"/></svg>(555) 318-6092</p>
    </div>
    <div class="services-tag">Services Provided :</div>
    <ul class="services">
      <li>Landscaping</li>
      <li>Lawn Maintenance</li>
      <li>Snow Removal</li>
      <li>Garden Center</li>
      <li>Tree Transplanting</li>
    </ul>
    <p class="address"><svg class="icon" viewBox="0 0 16 16"><circle cx="8" cy="8" r="8" fill="#fff"/><path d="M8 3a3 3 0 0 0-3 3c0 2.3 3 6 3 6s3-3.7 3-6a3 3 0 0 0-3-3z" fill="#0f4f0f"/><circle cx="8" cy="6" r="1.1" fill="#fff"/></svg>48, Orchard Lane Millbrook, OH-45999</p>
  </section>

</main>
</body>
</html>
```